Graphics for a 'guess the color' mobile phone project

I need the graphics (including source graphics in Illustrator or Photoshop) for the screens inside the game.

Please read the attached brief carefully, thanks!

```html
<!DOCTYPE html>
<html lang="en">
<head>
<meta charset="utf-8">
<title>Spin Wheel – Game Screens</title>
<link rel="stylesheet" href="https://fonts.googleapis.com/css2?family=Jost:ital,wght@0,500;0,600;0,700;1,700&display=swap">
<style>
  :root {
    --stage-top: #2a2a2a;
    --stage-bottom: #141414;
    --screen-bg: #f3f3f3;
    --header-bg: #ffffff;
    --ink: #333333;
    --cart-edge: #3a7bd5;
    --rim-light: #f6c75a;
    --rim-dark: #b97a14;
    --rim-edge: #6e4a10;
    --seg-1: #fff12a;
    --seg-2: #303e8e;
    --seg-3: #45f2e2;
    --seg-4: #f01c1c;
    --seg-5: #a636f2;
    --seg-6: #3ff22a;
    --seg-7: #ff4f1f;
    --seg-8: #2442ee;
    --hub: #7da6ef;
    --pointer: #4a4a4a;
    --btn-top: #7b2bb0;
    --btn-bottom: #3c0a6a;
    --ads-bg: #000000;
    --white: #ffffff;
    --card-top: #17b7f2;
    --card-bottom: #0a5fc2;
    --gold-top: #ffe45c;
    --gold-bottom: #d99a06;
  }
  * { box-sizing: border-box; }
  html, body {
    margin: 0;
    width: 1190px;
    height: 1200px;
    overflow: hidden;
  }
  body {
    background: linear-gradient(180deg, var(--stage-top), var(--stage-bottom));
    font-family: "Jost", sans-serif;
  }
  .screens {
    position: absolute;
    top: 182px;
    left: 59px;
    display: flex;
    gap: 80px;
  }
  .screen {
    width: 496px;
    height: 835px;
    display: block;
  }
  .screen-title { font-family: "Jost", sans-serif; font-weight: 500; font-size: 19px; fill: var(--ink); letter-spacing: 0.5px; }
  .back-arrow { fill: none; stroke: var(--ink); stroke-width: 2.2; stroke-linecap: round; stroke-linejoin: round; }
  .cart-icon { fill: none; stroke: var(--ink); stroke-width: 2.2; stroke-linejoin: round; stroke-linecap: round; }
  .segment-number { font-family: "Jost", sans-serif; font-weight: 600; font-size: 19px; fill: #111111; text-anchor: middle; dominant-baseline: central; }
  .spin-label { font-family: "Jost", sans-serif; font-weight: 600; font-size: 20px; fill: var(--white); text-anchor: middle; dominant-baseline: central; }
  .ads-label { font-family: "Jost", sans-serif; font-style: italic; font-weight: 700; font-size: 17px; fill: var(--white); text-anchor: middle; letter-spacing: 0.3px; }
  .win-title { font-family: "Jost", sans-serif; font-weight: 600; font-size: 31px; fill: #111111; text-anchor: middle; }
  .prize-label { font-family: "Jost", sans-serif; font-weight: 700; font-size: 30px; fill: #111111; text-anchor: middle; dominant-baseline: central; }
</style>
</head>
<body>
<main class="screens">

  <!-- Spin wheel screen -->
  <svg class="screen screen--spin" viewBox="0 0 310 522" role="img" aria-label="Spin wheel screen">
    <defs>
      <linearGradient id="rimGradient" x1="0" y1="0" x2="1" y2="1">
        <stop offset="0" stop-color="var(--rim-light)"/>
        <stop offset="1" stop-color="var(--rim-dark)"/>
      </linearGradient>
      <linearGradient id="buttonGradient" x1="0" y1="0" x2="0" y2="1">
        <stop offset="0" stop-color="var(--btn-top)"/>
        <stop offset="1" stop-color="var(--btn-bottom)"/>
      </linearGradient>
      <linearGradient id="swooshGradient" x1="0" y1="0" x2="1" y2="0">
        <stop offset="0" stop-color="#222" stop-opacity="0.9"/>
        <stop offset="1" stop-color="#999" stop-opacity="0"/>
      </linearGradient>
      <linearGradient id="cardGradient" x1="0" y1="0" x2="0" y2="1">
        <stop offset="0" stop-color="var(--card-top)"/>
        <stop offset="1" stop-color="var(--card-bottom)"/>
      </linearGradient>
      <linearGradient id="goldGradient" x1="0" y1="0" x2="0" y2="1">
        <stop offset="0" stop-color="var(--gold-top)"/>
        <stop offset="1" stop-color="var(--gold-bottom)"/>
      </linearGradient>
      <pattern id="scallop" width="8" height="8" patternUnits="userSpaceOnUse">
        <circle cx="4" cy="4" r="4" fill="var(--ads-bg)"/>
      </pattern>

      <g id="headerBar">
        <rect x="0" y="0" width="310" height="522" fill="var(--screen-bg)"/>
        <path d="M0 0 H252 V30 Q150 36 0 44 Z" fill="var(--header-bg)"/>
        <path d="M8 52 Q100 38 250 36 Q130 44 20 56 Q6 58 8 52 Z" fill="url(#swooshGradient)"/>
        <path class="back-arrow" d="M28 9 L19 18 L28 27"/>
        <text class="screen-title" x="152" y="27" text-anchor="middle">SPIN WHEEL</text>
        <path d="M248 0 H310 V52 Q300 42 268 40 Q252 38 248 30 Z" fill="var(--header-bg)" stroke="var(--cart-edge)" stroke-width="2"/>
        <g class="cart-icon">
          <path d="M263 9 H269 L274 26 H295 L299 13 H271"/>
          <circle cx="277" cy="32" r="2.4"/>
          <circle cx="292" cy="32" r="2.4"/>
        </g>
      </g>

      <g id="prizeWheel">
        <circle cx="155" cy="247" r="137" fill="url(#rimGradient)" stroke="var(--rim-edge)" stroke-width="1.5"/>
        <circle cx="155" cy="247" r="123" fill="none" stroke="var(--rim-edge)" stroke-width="2"/>
        <path d="M155 247 L155 127 A120 120 0 0 1 239.85 162.15 Z" fill="var(--seg-2)"/>
        <path d="M155 247 L239.85 162.15 A120 120 0 0 1 275 247 Z" fill="var(--seg-3)"/>
        <path d="M155 247 L275 247 A120 120 0 0 1 239.85 331.85 Z" fill="var(--seg-4)"/>
        <path d="M155 247 L239.85 331.85 A120 120 0 0 1 155 367 Z" fill="var(--seg-5)"/>
        <path d="M155 247 L155 367 A120 120 0 0 1 70.15 331.85 Z" fill="var(--seg-6)"/>
        <path d="M155 247 L70.15 331.85 A120 120 0 0 1 35 247 Z" fill="var(--seg-7)"/>
        <path d="M155 247 L35 247 A120 120 0 0 1 70.15 162.15 Z" fill="var(--seg-8)"/>
        <path d="M155 247 L70.15 162.15 A120 120 0 0 1 155 127 Z" fill="var(--seg-1)"/>
        <g stroke="var(--white)" stroke-width="1.5">
          <line x1="155" y1="127" x2="155" y2="367"/>
          <line x1="35" y1="247" x2="275" y2="247"/>
          <line x1="70.15" y1="162.15" x2="239.85" y2="331.85"/>
          <line x1="239.85" y1="162.15" x2="70.15" y2="331.85"/>
        </g>
        <text class="segment-number" x="120.6" y="163.8">1</text>
        <text class="segment-number" x="189.4" y="163.8">2</text>
        <text class="segment-number" x="238.2" y="212.6">3</text>
        <text class="segment-number" x="238.2" y="281.4">4</text>
        <text class="segment-number" x="189.4" y="330.2">5</text>
        <text class="segment-number" x="120.6" y="330.2">6</text>
        <text class="segment-number" x="71.8" y="281.4">7</text>
        <text class="segment-number" x="71.8" y="212.6">8</text>
        <circle cx="155" cy="247" r="58" fill="var(--white)" fill-opacity="0.6"/>
        <circle cx="155" cy="247" r="38" fill="var(--hub)" stroke="var(--white)" stroke-opacity="0.7" stroke-width="2"/>
        <path d="M155 225 L160.3 239.7 L175.9 240.2 L163.6 249.8 L167.9 264.8 L155 256 L142.1 264.8 L146.4 249.8 L134.1 240.2 L149.7 239.7 Z" fill="none" stroke="#111" stroke-width="2" stroke-linejoin="round"/>
        <path d="M138 107 H176 L157 150 Z" fill="var(--pointer)"/>
      </g>

      <g id="spinButton">
        <rect x="86" y="415" width="140" height="43" rx="6" fill="url(#buttonGradient)" stroke="#000" stroke-width="2"/>
        <text class="spin-label" x="156" y="437">SPIN</text>
      </g>

      <g id="adsBar">
        <rect x="0" y="476" width="310" height="8" fill="url(#scallop)"/>
        <rect x="0" y="480" width="310" height="42" fill="var(--ads-bg)"/>
        <text class="ads-label" x="155" y="506">ADVERTISEMENTS</text>
      </g>
    </defs>

    <use href="#headerBar"/>
    <use href="#prizeWheel"/>
    <use href="#spinButton"/>
    <use href="#adsBar"/>
  </svg>

  <!-- Prize won screen -->
  <svg class="screen screen--win" viewBox="0 0 310 522" role="img" aria-label="Prize won screen">
    <use href="#headerBar"/>
    <use href="#prizeWheel"/>
    <use href="#spinButton"/>
    <use href="#adsBar"/>
    <rect class="dim-overlay" x="0" y="0" width="310" height="522" fill="var(--white)" fill-opacity="0.6"/>

    <g class="prize-card">
      <rect x="44" y="419" width="220" height="60" rx="6" fill="var(--card-bottom)" fill-opacity="0.25"/>
      <rect x="44" y="112" width="220" height="307" rx="8" fill="url(#cardGradient)" stroke="#0a4f9a" stroke-width="1"/>
      <path d="M44 120 Q44 112 52 112 H256 Q264 112 264 120 V150 Q200 172 150 160 Q90 148 44 168 Z" fill="var(--white)"/>
      <text class="win-title" x="152" y="148">YOU WIN</text>
      <rect role="img" aria-label="Illustration of a cheerful cartoon winner holding up a golden trophy" x="62" y="170" width="184" height="170" rx="6" fill="#3ec8f6" fill-opacity="0.55"/>
      <rect x="64" y="352" width="178" height="51" rx="7" fill="url(#goldGradient)" stroke="#8a5a00" stroke-width="1.5"/>
      <text class="prize-label" x="153" y="378">5 images</text>
    </g>
  </svg>

</main>
</body>
</html>
```